"Folks Who Roam Wide" Adventure Travel Site

Folks Who Roam Wide is a travel site "instigating adventurous travel". It's ultimately a travel blog that features non-luxury, off-the beaten path, (often backpacking) trips with an open mind, honest writing, and sense of humor. My site does not book travel, only inspires the ideas for travel.

My objective: Transition from hobby travel blogger to cash generating travel blogger and create a recognizable brand. I need my site to look professionally done to attract readers, freelance jobs, other writers, and advertisers. Modes for user-interaction and increased traffic are very important.

The Look of the site: I want the logo to be displayed and the rest of the site match the look and feel of my logo. I like vintage and rugged. I'm not looking for a difficult layout, but want unique, creative graphics. I like vintage maps, postcards, rugged passports, passport stamps, cameras, photos, worn edges, etc.
The menu bar: Home-sweet-home, Meet Nora (sub cats: About and Contact), Travel Photos (Sub Cats: Africa, Asia, Australia and Oceania, Caribbean, Central America, Europe, Middle East, North America, South America) Travel Videos (same categories as Photos), and Media

Home-sweet-home: This will be my blog page. Photos are important to each post, so I don't want a layout that restricts this. I would like one column on the right side. The homepage must contain:

• RSS/Subscribe by e-mail , Share, and Follow buttons: If possible, I would like site "follow" and social network buttons to look like passport stamps, uniformly designed. (Twitter, Google+, Facebook, Subscribe via Email, RSS, LinkedIn) with a fun play on words like "follow me on my adventures"

• I would also like posts to be easy to share and very comment friendly. (tweet, stumbleupon, google+ dig/delicious etc. but I don't want these buttons to be too intrusive).

• "If you like this, you may also like" reader suggestions for posts

Right Column must include:

Heading:"Featured Travel Instigators (this should stand out)" with two categories, "Folks Who Roam Wide" and "Natives Steer Right"

Heading: "Categories (This should stand out)" will include the same regions in the photos drop down with sub-cats, also with "Travel Humor" and "Pages Are Dreamy" Category.

Widget (or whatever) that allows readers to view most popular posts, most recent posts, and comments

Widget for potential contributors that allows them to contact me: "Want to become a FWRW Travel Instigator?" I'd like this to open a page that explains what a FWRW travel instigator is, and then a contact option.

Room for: Facebook Likes Widget and Recent Tweets widget, badges, blog ranks, and ads

Travel Photos page: I would like users to be able to click on the menu drop down, choose from the 8 regions and view Albums with one cover photo, a title, and short description. Click on the Album and the first photo is large and all photos are thumbs underneath. Click and move through them all—pretty basic. I would like viewers to be able to leave comments for individual photos.

Travel Videos page: ditto the photo page layout except of course they're not albums.

current site: www.folkswhoroamwide.example (it's not pretty, please help!) :( Feel free to use any photos from site if you're so inspired.

Target Market(s)

off the beaten path adventure travelers 25-45

Industry/Entity Type

Travel

Requirements
Must have
• (described in detail in brief)
My logo. Easy to subscribe/follow/share. Great graphics. Vintage, rugged travel feel. I like vintage maps and postcards, photos, cameras, passports, and passport stamps.
Nice to have
Should not have
• I don't want it to be too girly. I have male readers and don't want them to be turned away by the appearance of the site.

```html
<!DOCTYPE html>
<html lang="en">
<head>
<meta charset="utf-8">
<title>Folks Who Roam Wide</title>
<link href="https://fonts.googleapis.com/css2?family=Oswald:wght@500;700&family=Open+Sans:wght@400;600;700&family=Cabin:wght@400;600&display=swap" rel="stylesheet">
<style>
:root{
  --bg:#e3c67f;
  --bg-dark:#d9b667;
  --nav:#e8972f;
  --nav-dark:#d27b1c;
  --nav-text:#6b3a0e;
  --cream:#fbf4df;
  --panel:#f3e3b6;
  --orange:#e8912f;
  --brown:#5a3510;
  --text:#806a4d;
  --link:#8a5a1a;
  --heading:#3a2a15;
  --green:#6fa63a;
  --ad-blue:#5bc2dc;
  --ad-dark:#1d1d1d;
}
*{box-sizing:border-box;margin:0;padding:0}
html,body{width:700px;height:1200px;overflow:hidden;background:var(--bg)}
body{font-family:"Open Sans",Arial,sans-serif;color:var(--text)}
.page{position:relative;width:700px;height:1200px;overflow:hidden;
  background:radial-gradient(circle at 30% 20%,#ead190 0,var(--bg) 40%,var(--bg-dark) 100%)}
.abs{position:absolute}

/* nav */
.main-nav{position:absolute;left:0;top:0;width:700px;height:50px;
  background:linear-gradient(#f0a848,var(--nav) 60%,var(--nav-dark));}
.main-nav a{position:absolute;top:14px;font-family:"Oswald",sans-serif;font-weight:700;
  font-size:14px;color:var(--nav-text);text-decoration:none}
.main-nav .active{left:80px;top:7px;width:66px;height:34px;background:#f1c98a;
  border:1px solid #c98a3c;text-align:center;line-height:32px}

/* brand */
.brand-mark{left:22px;top:58px;width:122px;height:122px;border-radius:50%;
  background:#c2722a;border:5px solid #a85d20}
.brand-name{left:14px;top:176px;font-family:"Oswald",sans-serif;font-weight:700;
  font-size:17px;color:#b9651f;letter-spacing:.2px}

/* subscribe */
.subscribe{left:38px;top:207px;width:174px;height:56px;background:var(--panel)}
.subscribe h4{position:absolute;left:10px;top:5px;font-size:9px;font-weight:600;color:var(--heading)}
.subscribe .field{position:absolute;left:10px;top:23px;width:103px;height:14px;background:#c6b48c;
  font-size:7px;color:#f4ecd8;padding:2px 4px}
.subscribe .btn{position:absolute;left:116px;top:23px;width:35px;height:14px;background:#4a2f14;
  color:#fff;font-size:7px;text-align:center;line-height:14px;border-radius:2px}
.subscribe .feeds{position:absolute;left:120px;top:44px;display:flex;gap:3px}
.subscribe .feeds i{width:7px;height:7px;background:var(--orange);display:block}
.subscribe .feeds i:nth-child(2){background:#6b8fc5}
.subscribe .feeds i:nth-child(3){background:#4d79b5}

/* slider */
.slider{left:216px;top:63px;width:472px;height:184px;background:#f6ecd3;
  box-shadow:2px 3px 6px rgba(80,50,10,.35);transform:rotate(.4deg)}
.slider .photo{position:absolute;left:9px;top:10px;width:454px;height:164px;
  background:linear-gradient(#141618 0,#1e1f1f 35%,#6b5227 60%,#c49a52 75%,#3a2c15 100%)}
.slider .caption{position:absolute;left:9px;top:18px;width:172px;height:30px;background:rgba(25,22,18,.85);
  font-family:"Cabin",sans-serif;font-size:13px;color:#e4c87e;padding:6px 9px}
.arrow{width:20px;height:20px;background:#fff;border:1px solid #999}
.arrow svg{display:block}

/* content */
.content{left:35px;top:262px;width:470px;height:883px;background:var(--cream)}
.post{position:absolute;left:0;width:470px}
.count{position:absolute;left:8px;top:12px;width:14px;height:10px;background:var(--green);
  color:#fff;font-size:7px;font-weight:700;text-align:center;line-height:10px}
.post h2{position:absolute;left:30px;top:8px;font-family:"Cabin",sans-serif;font-weight:400;
  font-size:13.5px;color:var(--heading)}
.post .meta{position:absolute;left:0;top:27px;width:455px;height:15px;background:var(--orange);
  font-size:7px;color:#fff;text-align:right;padding:3px 10px 0 0}
.post .meta b{font-weight:400;color:#fde7c4}
.avatar{position:absolute;left:416px;top:2px;width:24px;height:24px;background:#fff;border:1px solid #888}
.avatar::after{content:"";position:absolute;left:3px;top:3px;width:16px;height:16px;background:#8e8e8e}
.frame{position:absolute;left:45px;width:136px;background:#fff;padding:7px;
  border:2px dashed #e5dccb;box-shadow:0 0 2px rgba(0,0,0,.15)}
.frame div{width:100%;height:100%}
.post p{position:absolute;font-size:7.2px;line-height:11px;color:var(--text);text-align:justify}
.post .wide{left:45px;width:410px}
.post .pull{font-size:9px;line-height:15px;color:var(--link);text-decoration:underline}
.post .more{position:absolute;left:400px;font-size:8.5px;color:var(--heading)}
.post .serif{font-family:Georgia,"Times New Roman",serif;font-size:7.4px}
.divider{position:absolute;left:0;width:460px;border-top:1px dashed #c8b99a}

.stamps{position:absolute;left:-4px}
.stamp{width:18px;height:18px;margin-bottom:13px;transform:rotate(40deg);
  border:2px dotted #fff;outline:1px solid #ddd;box-shadow:1px 1px 2px rgba(0,0,0,.25)}
.s1{background:#8fd3e8}.s2{background:#2f5c9a}.s3{background:#3a85b8}
.s4{background:#ec8a2c}.s5{background:#f1f1f1}.s6{background:#5b86c2}

.pager{position:absolute;left:27px;top:858px;width:430px;font-size:7px;color:var(--heading);display:flex;align-items:center}
.pager span{margin-right:9px}
.pager .cur{background:#7d6444;color:#fff;padding:1px 4px}
.pager .top{position:absolute;left:372px;text-decoration:underline}

/* sidebar */
.banner{width:174px;height:30px;background:linear-gradient(#d9b37a,#c8995a);
  font-family:"Oswald",sans-serif;font-weight:700;font-size:12px;color:#fdf1d6;
  padding:6px 0 0 16px;box-shadow:1px 2px 3px rgba(80,50,10,.3)}
.side-item{width:168px;height:28px;border-bottom:1px solid #c9a866;font-family:"Cabin",sans-serif;
  font-size:10.5px;color:var(--brown);padding:6px 0 0 30px;position:absolute}
.side-item::before{content:"";position:absolute;left:12px;top:11px;width:10px;height:1px;background:var(--brown);
  box-shadow:0 -2px 0 var(--brown),0 2px 0 var(--brown)}
.caret{position:absolute;right:50px;top:12px;border:3px solid transparent;border-top:4px solid var(--brown)}

.tabs{left:513px;top:458px;width:176px;height:193px;background:#fdf7e6;border:2px solid #e9c587}
.tabs .bar{display:flex;height:22px;border-bottom:2px solid var(--orange)}
.tabs .bar span{font-size:9.5px;color:#2d2014;padding:4px 5px 0;border-right:1px solid #c8a86e}
.tabs .bar .on{background:var(--orange);color:#fff}
.tabs ul{list-style:none;padding:6px 10px 0 10px}
.tabs li{font-size:7.4px;line-height:11px;color:#9a6420;padding:0 0 6px 10px;border-bottom:1px dashed #d8c8a6;
  margin-bottom:6px;position:relative}
.tabs li::before{content:"";position:absolute;left:0;top:4px;width:3px;height:3px;background:#9a6420}
.ribbon{left:640px;top:463px;width:60px;height:13px;background:var(--orange);transform:rotate(40deg);
  font-size:6px;color:#fff;text-align:center;line-height:13px}

.likebox{left:513px;top:668px;width:176px;height:158px;background:var(--cream)}
.likebox .head{position:absolute;left:5px;top:9px;font-size:8px;line-height:11px;color:var(--heading)}
.likebox .head b{color:#b06a1a;font-weight:400}
.likebox .sub{position:absolute;left:5px;top:41px;font-size:5px;color:#555}
.likebox .btn{position:absolute;left:120px;top:39px;width:46px;height:11px;background:#eee;border:1px solid #bbb;
  font-size:6px;line-height:9px;padding-left:10px;color:#333}
.faces{position:absolute;left:5px;top:58px;display:grid;grid-template-columns:repeat(5,27px);gap:4px 6px}
.faces div{font-size:5px;text-align:center;color:#555}
.faces i{display:block;width:27px;height:27px;margin-bottom:2px}

.ads-label{left:513px;top:834px;font-size:8.5px;color:var(--heading)}
.ads-nav{left:675px;top:834px;font-size:8px;color:var(--heading)}
.ad{left:512px;top:851px;width:176px;height:210px;background:#fff;border:3px solid #2a2a2a;
  font-family:"Oswald",sans-serif;color:var(--ad-dark);text-align:center}
.ad .year{font-size:46px;line-height:48px;margin-top:8px;font-weight:700}
.ad .name{font-size:16px;line-height:16px;font-weight:700}
.ad .band{margin:8px auto 0;width:126px;background:var(--ad-blue);font-size:10px;line-height:14px;padding:4px 0;font-weight:500}
.ad .city{margin:6px auto 0;width:150px;height:44px;background:linear-gradient(#c8dc9c,#9cc25a)}
.ad .cta{position:absolute;left:6px;bottom:4px;width:158px;height:13px;background:#3a3a3a;color:#fff;font-size:8.5px;line-height:13px}

.follow{left:0;top:515px;width:28px;height:100px;background:linear-gradient(90deg,#c77a2a,#e39a44);
  border-radius:0 5px 5px 0}
.follow span{position:absolute;left:4px;top:8px;writing-mode:vertical-rl;font-family:"Oswald",sans-serif;
  font-weight:700;font-size:10px;color:#fbe6c3}
.follow i{position:absolute;left:5px;top:78px;width:16px;height:16px;border-radius:50%;background:#6cc3e4}

.footer{left:48px;top:1155px;font-size:6.5px;line-height:16px;color:var(--heading)}
.footer-stamps{left:515px;top:1160px;display:flex;gap:10px}
.footer-stamps .stamp{margin:0}
</style>
</head>
<body>
<div class="page">

  <nav class="main-nav">
    <a class="active" href="#">Home</a>
    <a href="#" style="left:185px">Meet Nora</a>
    <a href="#" style="left:300px">Travel Photos</a>
    <a href="#" style="left:434px">Travel Videos</a>
    <a href="#" style="left:568px">Media</a>
  </nav>

  <div class="abs brand-mark" aria-hidden="true"></div>
  <div class="abs brand-name">FOLKS WHO ROAM WIDE</div>

  <div class="abs subscribe">
    <h4>SUBSCRIBE</h4>
    <div class="field">Enter your mail ID</div>
    <div class="btn">Subscribe</div>
    <div class="feeds"><i></i><i></i><i></i></div>
  </div>

  <div class="abs slider">
    <div class="photo" role="img" aria-label="Night photo of an illuminated stone castle"></div>
    <div class="caption">Lorem Ipsum Contantry</div>
  </div>
  <div class="abs arrow" style="left:208px;top:145px"><svg width="18" height="18"><path d="M12 4 L6 9 L12 14Z" fill="#222"/></svg></div>
  <div class="abs arrow" style="left:674px;top:145px"><svg width="18" height="18"><path d="M6 4 L12 9 L6 14Z" fill="#222"/></svg></div>

  <main class="abs content">
    <article class="post" style="top:10px">
      <span class="count">32</span>
      <h2>The standard chunk of used since the 1500s</h2>
      <div class="avatar"></div>
      <div class="meta">Posted on : 26.8.2011 &nbsp;by <b>RJ Ward</b></div>
      <div class="stamps" style="top:58px"><div class="stamp s1"></div><div class="stamp s2"></div><div class="stamp s3"></div><div class="stamp s4"></div><div class="stamp s5"></div><div class="stamp s6"></div></div>
      <div class="frame" style="top:53px;height:146px"><div role="img" aria-label="Portrait photo of a smiling traveler outdoors" style="background:linear-gradient(135deg,#2f3a2a,#6f8a4a 60%,#b9c98a)"></div></div>
      <p style="left:199px;top:52px;width:253px">It is a long established fact that a reader will be distracted by the readable content of a page when looking at its layout. The point of using Lorem Ipsum is that it has a more-or-less normal distribution of letters, as opposed to using 'Content here, content here', making it look like readable English.</p>
      <p style="left:199px;top:110px;width:253px">Many desktop publishing packages and web page editors now use Lorem Ipsum as their default model text, and a search for 'lorem ipsum' will uncover many web sites still in their infancy.</p>
      <p class="pull" style="left:199px;top:164px;width:253px;text-align:left">The point of using Lorem Ipsum is that it has a more-or-less normal distribution of letters,</p>
      <p class="wide" style="top:207px">There are many variations of passages of Lorem Ipsum available, but the majority have suffered alteration in some form, by injected humour, or randomised words which don't look even slightly believable. If you are going to use a passage of Lorem Ipsum, you need to be sure there isn't anything embarrassing hidden in the middle of text.</p>
      <p class="wide" style="top:256px">All the Lorem Ipsum generators on the Internet tend to repeat predefined chunks as necessary, making this the first true generator on the Internet. It uses a dictionary of over 200 Latin words, combined with a handful of model sentence structures, to generate Lorem Ipsum which looks reasonable. The generated Lorem Ipsum is therefore always free from repetition, injected humour, or non-characteristic words etc.</p>
      <span class="more" style="top:308px">Read more...</span>
    </article>
    <div class="divider" style="top:337px"></div>

    <article class="post" style="top:345px">
      <span class="count">32</span>
      <h2>The standard chunk of used since the 1500s</h2>
      <div class="avatar"></div>
      <div class="meta">Posted on : 26.8.2011 &nbsp;by <b>RJ Ward</b></div>
      <div class="stamps" style="top:60px"><div class="stamp s1"></div><div class="stamp s2"></div><div class="stamp s3"></div><div class="stamp s4"></div><div class="stamp s5"></div><div class="stamp s6"></div></div>
      <div class="frame" style="top:56px;height:146px"><div role="img" aria-label="Photo of a white petal-shaped temple under a blue sky" style="background:linear-gradient(#2f7fd0,#8fc0ec 45%,#f2f2f2 60%,#c9c2b0 80%,#9a6a50)"></div></div>
      <p style="left:199px;top:53px;width:253px">It is a long established fact that a reader will be distracted by the readable content of a page when looking at its layout. The point of using Lorem Ipsum is that it has a more-or-less normal distribution of letters, as opposed to using 'Content here, content here', making it look like readable English.</p>
      <p style="left:199px;top:115px;width:253px">Many desktop publishing packages and web page editors now use Lorem Ipsum as their default model text, and a search for 'lorem ipsum' will uncover many web sites still in their infancy. Various versions have evolved over the years, sometimes by accident, sometimes on purpose (injected humour and the like).</p>
      <p class="pull" style="left:199px;top:178px;width:253px;text-align:left">The point of using Lorem Ipsum is that it has a more-or-less normal distribution of letters,</p>
      <span class="more" style="top:228px">Read more...</span>
    </article>
    <div class="divider" style="top:593px"></div>

    <article class="post" style="top:600px">
      <span class="count">32</span>
      <h2>The standard chunk of used since the 1500s</h2>
      <div class="avatar"></div>
      <div class="meta">Posted on : 26.8.2011 &nbsp;by <b>RJ Ward</b></div>
      <div class="stamps" style="top:60px"><div class="stamp s1"></div><div class="stamp s2"></div><div class="stamp s3"></div><div class="stamp s4"></div><div class="stamp s5"></div><div class="stamp s6"></div></div>
      <div class="frame" style="top:56px;height:150px"><div role="img" aria-label="Photo of a sailboat on a tropical beach with palm trees" style="background:linear-gradient(#2a86d8,#7fc4ec 40%,#36b8c0 60%,#e9dcc0 80%,#cbb894)"></div></div>
      <p class="serif" style="left:199px;top:53px;width:253px">It is a long established fact that a reader will be distracted by the readable content of a page when looking at its layout. The point of using Lorem Ipsum is that it has a more-or-less normal distribution of letters, as opposed to using 'Content here, content here', making it look like readable English.</p>
      <p class="serif" style="left:199px;top:115px;width:253px">Many desktop publishing packages and web page editors now use Lorem Ipsum as their default model text, and a search for 'lorem ipsum' will uncover many web sites still in their infancy. Various versions have evolved over the years, sometimes by accident, sometimes on purpose (injected humour and the like).</p>
      <p class="pull serif" style="left:199px;top:180px;width:253px;font-size:9.5px">The point of using Lorem Ipsum is that it has a</p>
      <span class="more" style="top:222px">Read more...</span>
    </article>

    <nav class="pager">
      <span>PAGE</span>
      <svg width="12" height="10" style="margin-right:9px"><path d="M11 5H3M6 1L2 5L6 9" stroke="#3a8ad0" stroke-width="2" fill="none"/></svg>
      <span>1</span><span>2</span><span>3</span><span>4</span><span>5</span><span>6</span><span class="cur">7</span><span>8</span><span>9</span><span>........</span><span>103</span><span>104</span><span>105</span><span>106</span>
      <svg width="12" height="10"><path d="M1 5H9M6 1L10 5L6 9" stroke="#3a8ad0" stroke-width="2" fill="none"/></svg>
      <span class="top">GO TO TOP</span>
    </nav>
  </main>

  <aside>
    <div class="abs banner" style="left:515px;top:265px;transform:rotate(-1deg)">Featured Travel Instigaters</div>
    <div class="side-item" style="left:522px;top:297px">Folks Who Roam Wide</div>
    <div class="side-item" style="left:522px;top:326px">Natives Steer Right</div>
    <div class="abs banner" style="left:515px;top:360px;transform:rotate(-1deg)">Categories</div>
    <div class="side-item" style="left:522px;top:396px">Travel Humor<span class="caret"></span></div>
    <div class="side-item" style="left:522px;top:425px">Pages Are Dreamy<span class="caret" style="right:34px"></span></div>

    <div class="abs tabs">
      <div class="bar"><span class="on">Popular</span><span>Recent</span><span>Comments</span></div>
      <ul>
        <li>Sections 1.10.32 and 1.10.33 from "de Finibus Bonorum et Malorum"</li>
        <li>Varro are also reproduced in their exact original form, accompanied</li>
        <li>English versions from the 1914 translation by H. Rowan.</li>
        <li>There are many variations of passages of Lorem Ipsum available</li>
        <li>Lorem Ipsum has been the industry's</li>
      </ul>
    </div>
    <div class="abs ribbon">POSTS</div>

    <div class="abs likebox">
      <div class="head">Like our page and win a bundle of <b style="color:var(--heading);font-weight:700">150 files</b><br>collection of our best graphics <b>?</b></div>
      <div class="sub">347 people like <b>Poster Nest</b>.</div>
      <div class="btn">Like</div>
      <div class="faces">
        <div><i style="background:#b8a88c"></i>Nadia</div>
        <div><i style="background:#8a7f70"></i>Tomas</div>
        <div><i style="background:#6f8a5a"></i>Arun</div>
        <div><i style="background:#7a5a45"></i>Martin</div>
        <div><i style="background:#d8d26a"></i>Maya</div>
        <div><i style="background:#c6a78a"></i>Kavi</div>
        <div><i style="background:#9a9a9a"></i>Karim</div>
        <div><i style="background:#4a4a4a"></i>Mira</div>
        <div><i style="background:#7a6a5a"></i>Samir</div>
        <div><i style="background:#9ab88a"></i>Malik</div>
      </div>
    </div>

    <div class="abs ads-label">Sponsored Ads</div>
    <div class="abs ads-nav">&lsaquo; &rsaquo;</div>
    <div class="abs ad">
      <div class="year">2011</div>
      <div class="name">TRAIL SUMMIT</div>
      <div class="name">CONFERENCE</div>
      <div class="band">· PORTLAND, OR ·<br>OCTOBER 27-29</div>
      <div class="city" role="img" aria-label="Green city skyline illustration"></div>
      <div class="cta">LEARN MORE &amp; REGISTER &gt;</div>
    </div>
  </aside>

  <div class="abs follow"><span>FOLLOW ME</span><i></i></div>

  <footer class="abs footer">Copyright @ 2011 www.folkswhoroamwide.example<br>All rights reserved</footer>
  <div class="abs footer-stamps">
    <div class="stamp s1"></div><div class="stamp s2"></div><div class="stamp s3"></div><div class="stamp s4"></div><div class="stamp s5"></div><div class="stamp s6"></div>
  </div>

</div>
</body>
</html>
```